New Bicycle shop business card

Hi!
I'm looking for a business card for my new proffesional bike mechanics shop. This shop is only for fixing broken bikes and not selling bikes.
Peferbly a modern and sleek and modern design.
Colors: black, grey, red, white
Information:
Name: Velowerkplaats Martens
Shop owner: Bart Martens & Sofie Vanhulle
Website: www.velowerkplaats-martens.be
Email: info@velowerkplaats-martens.be
Phone number: +32471936208
Street adres: Molenweg 57
9470 Sint-Ardenhove
Slogan/shop information: Herstellingen van alle merken.
Logo: see files.
Target Market(s)
People who seek a mechanic to fix or upgrade their bikes.
Contact Information for Business Card
Information:
Website: info@velowerkplaats-martens.be
9470 Sint-Ardenhove
Logo: see files.

```html
<!DOCTYPE html>
<html lang="nl">
<head>
<meta charset="utf-8">
<title>Velowerkplaats Martens – visitekaartje</title>
<link rel="stylesheet" href="https://fonts.googleapis.com/css2?family=Montserrat:wght@800&family=Open+Sans:wght@400;600;700&family=Kaushan+Script&display=swap">
<style>
  :root {
    --stage: #2b2e33;
    --ink: #111214;
    --charcoal: #2a2a2c;
    --steel: #5a5a5c;
    --silver: #a9a9ab;
    --mist: #d0d0d2;
    --paper: #ffffff;
    --signal: #e4283a;
    --text-dark: #1c1c1c;
    --text-grey: #7a7a7c;
  }
  * { box-sizing: border-box; margin: 0; padding: 0; }
  html, body { width: 1200px; height: 900px; overflow: hidden; }
  body {
    background: var(--stage);
    position: relative;
    font-family: "Open Sans", Arial, sans-serif;
  }

  /* ---------- front side ---------- */
  .card-front {
    position: absolute;
    left: 510px; top: 300px;
    width: 580px; height: 330px;
    border-radius: 26px;
    overflow: hidden;
    background: linear-gradient(160deg, var(--ink) 0%, var(--charcoal) 55%, var(--steel) 100%);
  }
  .card-front .brand {
    position: absolute;
    left: 0; right: 0; top: 108px;
    display: flex; align-items: center; justify-content: center; gap: 16px;
  }
  .brand-dot {
    flex: none;
    width: 22px; height: 22px; border-radius: 50%;
    background: var(--signal);
  }
  .card-front .brand-name {
    font-family: "Montserrat", Arial, sans-serif;
    font-weight: 800;
    font-size: 30px;
    letter-spacing: 1px;
    color: var(--paper);
    text-transform: uppercase;
  }
  .slogan-band {
    position: absolute;
    left: 0; right: 0; bottom: 0;
    height: 62px;
    background: linear-gradient(90deg, var(--silver), var(--mist) 40%, var(--silver));
    display: flex; align-items: center; justify-content: center;
  }
  .slogan {
    font-family: "Kaushan Script", cursive;
    font-size: 30px;
    color: var(--ink);
  }

  /* ---------- back side ---------- */
  .card-back {
    position: absolute;
    left: 110px; top: 170px;
    width: 330px; height: 560px;
    border-radius: 26px;
    overflow: hidden;
    background: var(--paper);
  }
  .card-back .frame {
    position: absolute; inset: 0;
    width: 100%; height: 100%;
  }
  .card-back .brand {
    position: absolute;
    left: 30px; top: 46px;
    display: flex; align-items: center; gap: 10px;
  }
  .card-back .brand-dot { width: 16px; height: 16px; }
  .card-back .brand-name {
    font-family: "Montserrat", Arial, sans-serif;
    font-weight: 800;
    font-size: 17px;
    color: var(--text-dark);
    text-transform: uppercase;
    line-height: 1.15;
  }
  .owners {
    position: absolute;
    left: 30px; top: 118px;
    font-weight: 700;
    font-size: 13px;
    line-height: 1.45;
    color: var(--text-dark);
  }
  .divider {
    position: absolute;
    left: 30px; top: 196px;
    width: 270px; height: 1px;
    background: var(--mist);
  }
  .contact {
    position: absolute;
    left: 30px; top: 216px;
    list-style: none;
    color: var(--text-grey);
    font-size: 13.5px;
  }
  .contact li {
    display: flex; align-items: flex-start; gap: 10px;
    margin-bottom: 9px;
    line-height: 1.4;
  }
  .contact .icon {
    flex: none;
    width: 18px; height: 18px;
    margin-top: 1px;
  }
</style>
</head>
<body>

  <section class="card-back" aria-label="Achterzijde visitekaartje">
    <svg class="frame" viewBox="0 0 330 560" preserveAspectRatio="none" aria-hidden="true">
      <rect width="330" height="560" fill="#121214"/>
      <polygon points="0,0 330,0 330,360 300,560 60,560 0,340" fill="#a9a9ab"/>
      <polygon points="0,0 330,0 330,370 292,560 68,560 0,352" fill="#e4283a"/>
      <polygon points="0,0 330,0 330,382 282,560 78,560 0,366" fill="#ffffff"/>
    </svg>

    <div class="brand">
      <span class="brand-dot"></span>
      <span class="brand-name">Velowerkplaats<br>Martens</span>
    </div>

    <p class="owners">Velowerkplaats Martens<br>Shop owner: Bart Martens<br>&amp; Sofie Vanhulle</p>

    <div class="divider"></div>

    <ul class="contact">
      <li>
        <svg class="icon" viewBox="0 0 18 18" aria-hidden="true"><rect width="18" height="18" rx="2" fill="#7a7a7c"/><path d="M9 3.5a3.5 3.5 0 0 0-3.5 3.5c0 2.6 3.5 7 3.5 7s3.5-4.4 3.5-7A3.5 3.5 0 0 0 9 3.5zm0 4.8a1.3 1.3 0 1 1 0-2.6 1.3 1.3 0 0 1 0 2.6z" fill="#fff"/></svg>
        <span>Molenweg 57<br>9470 Sint-Ardenhove</span>
      </li>
      <li>
        <svg class="icon" viewBox="0 0 18 18" aria-hidden="true"><rect width="18" height="18" rx="2" fill="#7a7a7c"/><path d="M6 4l2 2.5-1.2 1.3a7 7 0 0 0 3.4 3.4l1.3-1.2L14 12l-1.4 1.8C8.5 13.5 4.5 9.5 4.2 5.4z" fill="#fff"/></svg>
        <span>+32471936208</span>
      </li>
      <li>
        <svg class="icon" viewBox="0 0 18 18" aria-hidden="true"><rect width="18" height="18" rx="2" fill="#7a7a7c"/><rect x="3.5" y="5" width="11" height="8" fill="none" stroke="#fff" stroke-width="1.3"/><path d="M3.5 5l5.5 4.5L14.5 5" fill="none" stroke="#fff" stroke-width="1.3"/></svg>
        <span>info@velowerkplaats-martens.be</span>
      </li>
      <li>
        <svg class="icon" viewBox="0 0 18 18" aria-hidden="true"><rect width="18" height="18" rx="2" fill="#7a7a7c"/><circle cx="9" cy="9" r="5" fill="none" stroke="#fff" stroke-width="1.2"/><ellipse cx="9" cy="9" rx="2.2" ry="5" fill="none" stroke="#fff" stroke-width="1"/><path d="M4 9h10" stroke="#fff" stroke-width="1"/></svg>
        <span>www.velowerkplaats-martens.be</span>
      </li>
    </ul>
  </section>

  <section class="card-front" aria-label="Voorzijde visitekaartje">
    <div class="brand">
      <span class="brand-dot"></span>
      <span class="brand-name">Velowerkplaats Martens</span>
    </div>
    <div class="slogan-band">
      <p class="slogan">Herstellingen van alle merken</p>
    </div>
  </section>

</body>
</html>
```